Snack package design "Driftwood Curled Crisp"

Looking to create a fun package design of snack. Snack is sweet and crunchy; great for people that wants to munch on stuff. Name of the Snack is "Driftwood Curled Crisp". The net weight should be 16oz (453 grams). I added brand "TMvR" Too Mellow Vast Rays on the file. I also added picture of the snack. Package will be a pouch type.

Target Market(s)

People that like sweet snacks

Industry/Entity Type

Food snacks

Requirements
Must have
• Name of Snack "Driftwood Curled Crisp" and logo of company on top left.
Nice to have
• something that's simple and clean design

```html
<!DOCTYPE html>
<html lang="en">
<head>
<meta charset="utf-8">
<title>Driftwood Curled Crisp – Pouch Front</title>
<link rel="stylesheet" href="https://fonts.googleapis.com/css2?family=Open+Sans:wght@600;800&family=Courgette&family=Oswald:wght@400&family=Tinos&display=swap">
<style>
  :root {
    --backdrop: #cfd8db;
    --pouch-black: #1c1c1c;
    --pouch-seam: #2a2a2a;
    --snack-light: #e4884a;
    --snack-mid: #c9622f;
    --snack-deep: #9c4420;
    --leaf-green: #6d9f3c;
    --leaf-light: #8fbc58;
    --brand-green: #5e9a2e;
    --ink-white: #f4f4f4;
    --ink-outline: #1a1a1a;
  }
  * { box-sizing: border-box; margin: 0; padding: 0; }
  html, body {
    width: 1200px; height: 835px; overflow: hidden;
    background: var(--backdrop);
  }
  .canvas { position: relative; width: 1200px; height: 835px; }

  .pouch {
    position: absolute; left: 430px; top: 126px;
    width: 340px; height: 583px;
    background: var(--pouch-black);
    border-radius: 14px 14px 8px 8px;
    overflow: hidden;
  }
  .zipper-seal {
    position: absolute; left: 0; right: 0; top: 20px; height: 52px;
    border-top: 2px solid var(--pouch-seam);
    border-bottom: 2px solid var(--pouch-seam);
  }

  .brand-tagline {
    position: absolute; top: 74px; left: 0; right: 0;
    text-align: center;
    font: 600 23px/1 "Open Sans", sans-serif;
    color: var(--brand-green);
  }
  .brand-mark {
    position: absolute; top: 108px; left: 0; right: 0;
    display: flex; justify-content: center; align-items: center; gap: 12px;
  }
  .brand-dot {
    width: 34px; height: 34px; border-radius: 50%;
    background: var(--brand-green);
  }
  .brand-name {
    font: 800 52px/1 "Open Sans", sans-serif;
    color: var(--ink-white);
    letter-spacing: 2px;
  }

  .snack-photo {
    position: absolute; left: 11px; right: 10px; top: 208px; height: 300px;
    background:
      radial-gradient(circle at 30% 40%, var(--snack-light), transparent 55%),
      radial-gradient(circle at 75% 65%, var(--snack-light), transparent 50%),
      linear-gradient(160deg, var(--snack-mid), var(--snack-deep));
  }

  .title-panel {
    position: absolute; left: 46px; width: 250px; top: 200px; height: 90px;
    background: var(--pouch-black);
    border-radius: 0 0 12px 12px;
    display: flex; flex-direction: column; justify-content: center; align-items: center;
  }
  .product-name {
    font: 400 29px/1.1 "Courgette", cursive;
    color: var(--ink-white);
    text-align: center;
  }

  .flavour-claim {
    position: absolute; top: 338px; left: 0; right: 0;
    text-align: center;
    font: 400 27px/1 "Oswald", sans-serif;
    color: var(--ink-white);
    -webkit-text-stroke: 1px var(--ink-outline);
    text-shadow: 0 0 3px var(--ink-outline), 1px 1px 0 var(--ink-outline);
  }

  .bottom-wave { position: absolute; left: 0; top: 0; width: 340px; height: 583px; }

  .net-weight {
    position: absolute; top: 537px; left: 0; right: 0;
    text-align: center;
    font: 400 12px/1 "Tinos", serif;
    color: var(--ink-white);
  }
</style>
</head>
<body>
<div class="canvas">
  <div class="pouch">
    <div class="zipper-seal"></div>

    <div class="brand-tagline">Too Mellow Vast Rays</div>
    <div class="brand-mark">
      <span class="brand-dot"></span>
      <span class="brand-name">TMvR</span>
    </div>

    <div class="snack-photo" role="img" aria-label="Photo of golden-orange curled crisp snack pieces piled together"></div>

    <div class="title-panel">
      <h1 class="product-name">Driftwood<br>Curled Crisp</h1>
    </div>

    <p class="flavour-claim">Sweet And Crunchy</p>

    <svg class="bottom-wave" viewBox="0 0 340 583" aria-hidden="true">
      <path d="M0 452 C 90 425, 200 440, 340 492 L340 583 L0 583 Z" fill="var(--leaf-green)"/>
      <path d="M0 460 C 90 436, 200 452, 340 504 L340 583 L0 583 Z" fill="var(--pouch-black)"/>
    </svg>

    <p class="net-weight">Net Weight:16oz (453 grams)</p>
  </div>
</div>
</body>
</html>
```